Wordpress Design For Financial Investment Company

//** NEW WIREFRAME ADDED TO HELP WITH LAYOUT ISSUES. PLEASE REFER TO WIREFRAME IN ATTACHED FILES. NO DESIGN WILL BE CONSIDERED IF IT DOES NOT FOLLOW THE WIREFRAME. **//
//** PLEASE READ THE ENTIRE BRIEF INCLUDING ALL UPDATES TO THE BRIEF. THE CLIENT IS VERY SPECIFIC ABOUT WHAT THEY WANT AND I'VE COVERED SEVERAL THINGS IN THE UPDATES. THERE IS ALSO A VIDEO UPDATE THAT HAS SOME VALUABLE INFORMATION IN IT FOR THIS CONTEST. **//
The client is an investment advisor who needs a new website designed. The current site is http://www.velmorfield.net.
The client wants the site to be green to match the attached logo.
The home page should have relevant images in the rotator. No people hugging! This is a financial investment site, not a family counseling site.
Also, the client wants 4 buttons on the home page to highlight the 4 main areas they focus on:
Investment Advice and Education
General Financial Planning
Retirement Planning
401K Planning
The top right area of the site needs to have their phone number, a call to action, and 2 buttons.
Their phone number is 303-418-7639
The call to action should say something like "Call for a free consultation!"
The buttons need to say:
Login To Your Bluvexa Account
Login To Your Quillbrook Account
The final design should communicate professionalism, financial safety and growth.
Main navigation should be:
Home
About Us
Associates
Services
Contact
Mission Statement (Could also be "Our Mission")
This is a site that the client likes: http://www.pwkinvestmentconsulting.com/
Updates
The designs should not have:
Newsletter content. A newsletter sign up is fine
Learning Center
Calculators
Stock prices/tickers
The design should have a contact form on the page.
I have talked to my client and have some updates. I did a video update because I thought it would be easier to show what I'm trying to get across.
Reason: I am going to be extending the contest a few more days. I'm still not getting quite what I want and very few people are even trying to follow the creative brief and the updates to it.
PLEASE read the entire brief and the updates. There is also a video I made that explains everything. I've also attached a wireframe.
Thanks!
Target Market(s)
People looking for a high-end financial investment company.
Industry/Entity Type
Investment
Requirements
Must have
- !!FOLLOW THE WIREFRAME FOR LAYOUT!!
!!THEIR LOGO!!
4 buttons to highlight their main practice areas
Phone number in the top right
"Free Consultation" call to action
2 Login buttons in the top right
A contact form on the page.
Should not have
- The designs should not have:
Learning Center
Calculators
Stock prices/tickers

```html
<!DOCTYPE html>
<html lang="en">
<head>
<meta charset="utf-8">
<title>Velmorfield Financial, Inc.</title>
<link rel="stylesheet" href="https://fonts.googleapis.com/css2?family=Cantarell:wght@400;700&family=Lato:wght@400;700&family=Arimo&display=swap">
<style>
:root{
  --green:#2f7a5c;
  --green-dark:#1f5c43;
  --green-deep:#174a35;
  --nav:#6fa48c;
  --ink:#1f5c43;
  --white:#ffffff;
  --photo-warm:#c9a78f;
}
*{box-sizing:border-box;margin:0;padding:0}
html,body{width:1000px;height:1200px;overflow:hidden}
body{
  position:relative;
  font-family:"Cantarell",sans-serif;color:var(--ink);
  background:
    linear-gradient(180deg,transparent 0,transparent 310px,rgba(255,255,255,.85) 360px,rgba(255,255,255,.95) 380px,rgba(255,255,255,.95) 820px,rgba(255,255,255,.6) 860px,transparent 920px),
    radial-gradient(ellipse at 30% 20%,#4f8f74,transparent 60%),
    radial-gradient(ellipse at 80% 90%,#3d7f63,transparent 55%),
    linear-gradient(160deg,#3c7e62,#2b6b50 50%,#3a7c60);
}
.abs{position:absolute}
.phone{left:700px;top:32px;width:180px;text-align:right;color:var(--white);white-space:nowrap}
.phone b{font-family:"Cantarell",serif;font-size:17px;font-weight:700;display:block;line-height:20px}
.phone small{font-family:"Lato",sans-serif;font-size:7.5px;font-weight:700;letter-spacing:.1px;display:block;line-height:10px}
.brace{position:absolute}
.nav{display:flex;gap:3px}
.nav a{height:36px;display:flex;align-items:center;justify-content:center;
  background:var(--nav);border:2px solid var(--green-dark);border-radius:7px;
  color:var(--white);font-family:"Lato",sans-serif;font-size:9.5px;font-weight:700;text-decoration:none;
  box-shadow:inset 0 0 0 1px rgba(255,255,255,.35)}
.brand{left:450px;top:50px;width:108px;text-align:center}
.brand .ring{width:70px;height:70px;border-radius:50%;background:#d9c3b2;border:4px solid #3a2a22;margin:0 auto}
.brand span{display:block;font-size:11px;font-weight:700;color:var(--white);margin-top:2px}
.quote{left:118px;top:126px;width:336px;color:var(--white);font-family:"Lato",sans-serif;font-size:10.5px;line-height:14px;text-align:right}
.quote p:first-child{text-align:left}
.login{top:138px;height:25px;background:var(--white);display:flex;align-items:center;gap:5px;padding:0 6px;
  font-size:10.5px;font-weight:700;color:var(--green-dark);white-space:nowrap}
.hero{left:108px;top:172px;width:789px;height:200px;background:var(--white);border-bottom:2px solid var(--green-dark);overflow:hidden}
.hero-photo{position:absolute;left:250px;top:0;width:539px;height:199px;
  background:linear-gradient(90deg,rgba(255,255,255,1) 0,rgba(240,236,235,.6) 20%,var(--photo-warm) 45%,#b9a3b4 70%,#b94a3a 100%)}
.hero-text{position:absolute;left:23px;top:26px;font-size:17px;line-height:21px;color:#2b3b33}
.mission{position:absolute;left:0;top:129px;width:388px;height:40px;background:linear-gradient(90deg,var(--green) 60%,rgba(47,122,92,.8));
  color:var(--white);font-size:19px;font-weight:700;padding:8px 0 0 23px;white-space:nowrap}
.card{width:380px;height:166px;border:1px solid var(--green-dark);border-radius:4px;background:var(--white)}
.card .photo{position:absolute;left:6px;top:6px;width:182px;height:107px;border:1px solid var(--green-dark)}
.card p{position:absolute;left:195px;top:27px;width:176px;font-size:13.5px;line-height:18px;color:#2a5a45;word-spacing:1px}
.card h2{position:absolute;left:6px;top:120px;width:367px;height:39px;border:1px solid var(--green-deep);border-radius:5px;
  background:linear-gradient(180deg,#5a9a7e,#3d7d61);color:var(--white);font-size:21px;font-weight:700;text-align:center;line-height:37px;
  white-space:nowrap;overflow:hidden;text-shadow:0 1px 2px rgba(0,0,0,.5)}
.panel{top:762px;width:380px;height:166px;background:var(--white);border-radius:6px}
.panel h3{font-size:18.5px;font-weight:700;color:var(--green-dark);white-space:nowrap}
.who h3{position:absolute;left:8px;top:6px;width:361px;padding-bottom:3px;border-bottom:1px solid var(--green-dark)}
.who p{position:absolute;left:15px;top:38px;width:245px;font-size:14px;line-height:18px;color:#2a4a3c}
.who .mark{position:absolute;left:262px;top:44px;width:106px;text-align:center}
.who .mark .ring{width:70px;height:70px;border-radius:50%;background:#d9c3b2;border:4px solid #3a2a22;margin:0 auto}
.who .mark span{display:block;font-size:11px;font-weight:700;color:var(--green-dark);margin-top:3px}
.contact h3{position:absolute;left:12px;top:4px}
.contact label{position:absolute;font-family:"Lato",sans-serif;font-size:10.5px;color:#2a5a45}
.contact .field{position:absolute;border:1px solid var(--green-dark);border-radius:3px;background:var(--white)}
.submit{position:absolute;left:179px;top:131px;width:51px;height:17px;background:var(--green-dark);border-radius:3px;color:#bfe0cf;
  font-size:11px;font-weight:700;text-align:center;line-height:17px}
.footer{left:105px;top:1132px;width:789px;border-top:1px solid rgba(255,255,255,.8);height:30px;font-family:"Arimo",sans-serif;color:var(--white);font-size:10.5px}
.footer nav span{position:absolute;top:9px;white-space:nowrap}
.footer .copy{position:absolute;right:0;top:9px;white-space:nowrap}
</style>
</head>
<body>

<svg class="brace" style="left:900px;top:12px" width="34" height="106" viewBox="0 0 34 106" aria-hidden="true">
  <path d="M4 2 C20 2 18 20 18 36 C18 48 22 52 32 53 C22 54 18 58 18 70 C18 86 20 104 4 104" fill="none" stroke="#fff" stroke-width="6"/>
</svg>
<svg class="brace" style="left:62px;top:116px" width="34" height="106" viewBox="0 0 34 106" aria-hidden="true">
  <path d="M30 2 C14 2 16 20 16 36 C16 48 12 52 2 53 C12 54 16 58 16 70 C16 86 14 104 30 104" fill="none" stroke="#fff" stroke-width="1.2"/>
</svg>

<div class="abs phone">
  <b><svg width="15" height="15" viewBox="0 0 20 20" style="vertical-align:-2px" aria-hidden="true"><circle cx="10" cy="10" r="9" fill="none" stroke="#fff" stroke-width="1.5"/><path d="M7 5 C5 7 6 12 10 15 L12 13 L10 11 L9 12 C8 11 8 9 9 8 L8 5Z" fill="#fff"/></svg> 303-418-7639</b>
  <small>FREE 20min PHONE CONSULTATION</small>
</div>

<nav class="abs nav" style="left:115px;top:85px">
  <a href="#" style="width:107px">HOME</a>
  <a href="#" style="width:119px">ABOUT US</a>
  <a href="#" style="width:103px">ASSOCIATES</a>
</nav>
<nav class="abs nav" style="left:559px;top:85px">
  <a href="#" style="width:102px">SERVICES</a>
  <a href="#" style="width:117px">CONTACT</a>
  <a href="#" style="width:103px">OUR MISSION</a>
</nav>

<div class="abs brand">
  <div class="ring"></div>
  <span>Velmorfield</span>
</div>

<div class="abs quote">
  <p>Always do right. This will astonish some people and gratify the rest.</p>
  <p>- Harlan Presk</p>
</div>

<div class="abs login" style="left:646px;width:119px">
  <svg width="11" height="15" viewBox="0 0 11 15" aria-hidden="true"><path d="M2.5 7V4.5a3 3 0 0 1 6 0V7" fill="none" stroke="#1f5c43" stroke-width="1.8"/><rect x="0.5" y="7" width="10" height="8" fill="#1f5c43"/></svg>Quillbrook Login
</div>
<div class="abs login" style="left:771px;width:119px">
  <svg width="11" height="15" viewBox="0 0 11 15" aria-hidden="true"><path d="M2.5 7V4.5a3 3 0 0 1 6 0V7" fill="none" stroke="#1f5c43" stroke-width="1.8"/><rect x="0.5" y="7" width="10" height="8" fill="#1f5c43"/></svg>Bluvexa Login
</div>

<section class="abs hero">
  <div class="hero-photo" role="img" aria-label="Grandparents helping a young child put a coin into a piggy bank"></div>
  <p class="hero-text">Integrity without knowledge<br>is weak and useless,<br>and knowledge without integrity<br>is dangerous and dreadful.</p>
  <div class="mission">View Our Mission Statement</div>
</section>

<article class="abs card" style="left:115px;top:391px">
  <div class="photo" role="img" aria-label="Woman reviewing a financial document" style="background:linear-gradient(90deg,#e6e2dc,#d98a6a 60%,#e9e4de)"></div>
  <p>Lorem ipsum dolor sit amet, consectetur adipisc-ing elit. Quisque at odio sit amet sapien sagittis mollis sit amet sit amet est.</p>
  <h2>Investment Advice &amp; Education</h2>
</article>
<article class="abs card" style="left:511px;top:391px">
  <div class="photo" role="img" aria-label="Businessman pointing at a market chart display" style="background:linear-gradient(90deg,#7f8fa4,#3f5f8a 55%,#8aa0b8)"></div>
  <p>Lorem ipsum dolor sit amet, consectetur adipisc-ing elit. Quisque at odio sit amet sapien sagittis mollis sit amet sit amet est.</p>
  <h2>General Financial Planning</h2>
</article>
<article class="abs card" style="left:115px;top:579px">
  <div class="photo" role="img" aria-label="Advisor meeting a couple at a laptop in a kitchen" style="background:linear-gradient(90deg,#5a4a44,#b8b0a6 50%,#4a6aa8)"></div>
  <p>Lorem ipsum dolor sit amet, consectetur adipisc-ing elit. Quisque at odio sit amet sapien sagittis mollis sit amet sit amet est.</p>
  <h2>Retirement Planning</h2>
</article>
<article class="abs card" style="left:511px;top:579px">
  <div class="photo" role="img" aria-label="Yellow box filled with banknotes labelled 401k" style="background:linear-gradient(135deg,#e8c23a,#d8a91e 55%,#e7d3b0)"></div>
  <p>Lorem ipsum dolor sit amet, consectetur adipisc-ing elit. Quisque at odio sit amet sapien sagittis mollis sit amet sit amet est.</p>
  <h2>401K Planning</h2>
</article>

<section class="abs panel who" style="left:115px">
  <h3>Who is VELMORFIELD Financial?</h3>
  <p>The mission of Velmorfield Financial, Inc, is to provide quality and value-oriented investment management services as well as individualized financial investment advice. We are committed to maintaining</p>
  <div class="mark"><div class="ring"></div><span>Velmorfield</span></div>
</section>

<section class="abs panel contact" style="left:511px">
  <h3>Contact Us</h3>
  <label style="left:12px;top:32px">Name</label>
  <div class="field" style="left:12px;top:47px;width:153px;height:17px"></div>
  <label style="left:12px;top:73px">Email</label>
  <div class="field" style="left:12px;top:89px;width:153px;height:17px"></div>
  <label style="left:12px;top:114px">Company</label>
  <div class="field" style="left:12px;top:131px;width:153px;height:17px"></div>
  <label style="left:179px;top:32px">Message</label>
  <div class="field" style="left:179px;top:47px;width:186px;height:79px"></div>
  <div class="submit">SUBMIT</div>
</section>

<footer class="abs footer">
  <nav>
    <span style="left:2px">HOME</span>
    <span style="left:54px">ABOUT US</span>
    <span style="left:134px">ASSOCIATES</span>
    <span style="left:215px">SERVICES</span>
    <span style="left:283px">CONTACT</span>
    <span style="left:349px">OUR MISSION</span>
  </nav>
  <span class="copy">© 2013 Velmorfield Financial Inc.</span>
</footer>

</body>
</html>
```